advertising board Morvalen BV

I have an advertisement spot in a small indoor football stadium, with the size of 1.00 x 22.00 meters. I want to show a design that stands out. My company works in Civil constructions and actually installs steel sheet piles and earth retaining walls in the most difficult to reach locations.

```html
<!DOCTYPE html>
<html lang="nl">
<head>
<meta charset="utf-8">
<title>Morvalen BV – reclamebord</title>
<link href="https://fonts.googleapis.com/css2?family=Exo+2:ital,wght@1,800&family=Montserrat:wght@400;600&display=swap" rel="stylesheet">
<style>
  :root{
    --page:#eceef0;
    --white:#ffffff;
    --rule:#3b3b3d;
    --brand-blue:#2a8fd8;
    --band-dark:#3b3b3e;
    --band-mid:#4a4a4e;
    --ink:#333335;
  }
  html,body{margin:0;padding:0;overflow:hidden;}
  body{width:1200px;height:764px;background:var(--page);position:relative;}
  .board{
    position:absolute;left:0;width:1200px;height:52px;
    background:var(--white);
    border-top:3px solid var(--rule);border-bottom:3px solid var(--rule);
    display:flex;
  }
  .board--top{top:300px;}
  .board--bottom{top:412px;}
  .unit{position:relative;width:600px;height:52px;}
  .unit__shapes{position:absolute;inset:0;}
  .brand-name{
    position:absolute;left:78px;top:4px;
    font-family:"Montserrat",sans-serif;font-weight:600;
    font-size:28px;line-height:32px;color:var(--brand-blue);
    white-space:nowrap;
  }
  .brand-tagline{
    position:absolute;left:79px;top:37px;
    font-family:"Montserrat",sans-serif;font-weight:400;
    font-size:7.4px;color:var(--ink);white-space:nowrap;
  }
  .contact{
    position:absolute;left:382px;width:216px;top:3px;text-align:center;color:var(--white);
  }
  .contact__phone{
    font-family:"Exo 2",sans-serif;font-style:italic;font-weight:800;
    font-size:24px;line-height:27px;letter-spacing:1px;
  }
  .contact__web{
    font-family:"Montserrat",sans-serif;font-weight:400;
    font-size:12.5px;line-height:16px;
  }
</style>
</head>
<body>

<div class="board board--top">
  <div class="unit">
    <svg class="unit__shapes" width="600" height="52" viewBox="0 0 600 52">
      <circle cx="44" cy="26" r="19" fill="var(--brand-blue)"/>
      <polygon points="374,5 600,5 600,47 374,47 386,26" fill="var(--band-dark)"/>
      <rect x="386" y="33" width="214" height="14" fill="var(--band-mid)"/>
    </svg>
    <div class="brand-name">Morvalen</div>
    <div class="brand-tagline">damwandconstructies - onderhoud - beschoeiingen - grondwerk</div>
    <div class="contact"><div class="contact__phone">030 412 67 58</div><div class="contact__web">www.morvalen.nl</div></div>
  </div>
  <div class="unit">
    <svg class="unit__shapes" width="600" height="52" viewBox="0 0 600 52">
      <circle cx="44" cy="26" r="19" fill="var(--brand-blue)"/>
      <polygon points="374,5 600,5 600,47 374,47 386,26" fill="var(--band-dark)"/>
      <rect x="386" y="33" width="214" height="14" fill="var(--band-mid)"/>
    </svg>
    <div class="brand-name">Morvalen</div>
    <div class="brand-tagline">damwandconstructies - onderhoud - beschoeiingen - grondwerk</div>
    <div class="contact"><div class="contact__phone">030 412 67 58</div><div class="contact__web">www.morvalen.nl</div></div>
  </div>
</div>

<div class="board board--bottom">
  <div class="unit">
    <svg class="unit__shapes" width="600" height="52" viewBox="0 0 600 52">
      <circle cx="44" cy="26" r="19" fill="var(--brand-blue)"/>
      <polygon points="374,5 600,5 600,47 374,47 386,26" fill="var(--band-dark)"/>
      <rect x="386" y="33" width="214" height="14" fill="var(--band-mid)"/>
    </svg>
    <div class="brand-name">Morvalen</div>
    <div class="brand-tagline">damwandconstructies - onderhoud - beschoeiingen - grondwerk</div>
    <div class="contact"><div class="contact__phone">030 412 67 58</div><div class="contact__web">www.morvalen.nl</div></div>
  </div>
  <div class="unit">
    <svg class="unit__shapes" width="600" height="52" viewBox="0 0 600 52">
      <circle cx="44" cy="26" r="19" fill="var(--brand-blue)"/>
      <polygon points="374,5 600,5 600,47 374,47 386,26" fill="var(--band-dark)"/>
      <rect x="386" y="33" width="214" height="14" fill="var(--band-mid)"/>
    </svg>
    <div class="brand-name">Morvalen</div>
    <div class="brand-tagline">damwandconstructies - onderhoud - beschoeiingen - grondwerk</div>
    <div class="contact"><div class="contact__phone">030 412 67 58</div><div class="contact__web">www.morvalen.nl</div></div>
  </div>
</div>

</body>
</html>
```